Book Cover: Quiet Bloom: Daily Practices For The Present Woman

I would like a full cover spread- front, back and spine as well as a stand alone front cover for Kindle for the book. Design a cover that mirrors the profound depth and dynamic energy of 'Quiet Bloom.' Envision a visual tapestry that draws readers into a transformative journey, where spirituality and self-care unite. Explore vibrant colors, intricate textures, and a sense of inner radiance that beckons readers to explore the book's rich wisdom within. See images for design inspiration attached. Even though some of the images are cartoon, I'd like the cover to be more serious than playful and very elegant.

About this book (back cover copy)
Are you ready to embark on a transformative journey and elevate your daily existence? "Quiet Bloom" is a treasure trove of practical yet profound rituals and wisdom from renowned self-care, healing, and spirituality experts.

Within these pages, you'll uncover a tapestry of guidance and insight from some of the world's most respected mentors. Their collective wisdom is your key to creating a sacred sanctuary within your everyday life.

From invigorating morning rituals to meditative practices, empowering affirmations, and transformative energy healing, you'll find a rich tapestry of tools to nurture a deeper connection with yourself and the universe.

Whether you're a seasoned practitioner or a newcomer to the world of self-care and spirituality, "Quiet Bloom" is your trusted companion on the journey to transform your life and elevate your daily experience. Open this book today and start your sacred, fulfilling adventure.

Colors
0094D4
00A9DD
6FCCEA
C7EBF8
E9F6FB
E54698
E96AAD
F1A4CE
F9D9EA
FCEFF6
6B429C
8869AF
B7A5CE
E3DAEB
F3F0F8

Requirements
Must have
• Title: Quiet Bloom: Subtitle: Daily Practices For The Present Woman Name of Publisher: Lantern Grove Publishing- Logo on the back Back cover copy

```html
<!DOCTYPE html>
<html lang="en">
<head>
<meta charset="utf-8">
<title>Quiet Bloom – Cover Spread</title>
<link rel="stylesheet" href="https://fonts.googleapis.com/css2?family=Great+Vibes&family=Marcellus&family=Marcellus+SC&family=Montserrat:wght@400&display=swap">
<style>
  :root {
    --canvas: #ffffff;
    --ink-light: #ffffff;
    --ink-soft: #fdf3ee;
    --ink-dark: #1e0d08;
    --shade-deep: #2a0805;
    --shade-red: #8e1a0c;
    --ember: #d2400f;
    --amber: #f28a1c;
    --gold: #f7c63a;
    --blush: #f6d9e2;
    --glow: #fff5f4;
    --mauve: #b5607a;
  }
  * { margin: 0; padding: 0; box-sizing: border-box; }
  html, body {
    width: 1200px; height: 1200px; overflow: hidden;
    background: var(--canvas);
  }
  .spread {
    position: absolute;
    left: 22px; top: 184px;
    width: 1156px; height: 832px;
    overflow: hidden;
    color: var(--ink-light);
  }
  .spread-photo {
    position: absolute; inset: 0;
    background:
      radial-gradient(ellipse 220px 260px at 880px 300px, var(--glow) 0%, var(--blush) 35%, rgba(246,217,226,0) 100%),
      radial-gradient(ellipse 180px 140px at 1040px 120px, var(--gold) 0%, rgba(247,198,58,0) 100%),
      radial-gradient(ellipse 260px 200px at 1080px 330px, var(--amber) 0%, rgba(242,138,28,0) 100%),
      radial-gradient(ellipse 170px 160px at 480px 300px, #c8b040 0%, rgba(200,176,64,0) 100%),
      radial-gradient(ellipse 200px 160px at 330px 420px, var(--mauve) 0%, rgba(181,96,122,0) 100%),
      radial-gradient(ellipse 300px 220px at 420px 600px, var(--ember) 0%, rgba(210,64,15,0) 100%),
      radial-gradient(ellipse 260px 200px at 760px 120px, #7a2412 0%, rgba(122,36,18,0) 100%),
      linear-gradient(180deg, rgba(42,8,5,0) 55%, var(--shade-deep) 100%),
      linear-gradient(90deg, var(--shade-deep) 0%, var(--shade-red) 40%, #a33518 70%, var(--shade-red) 100%);
  }
  .back-cover, .spine, .front-cover { position: absolute; top: 0; height: 100%; }
  .back-cover { left: 0; width: 555px; }
  .spine { left: 555px; width: 50px; }
  .front-cover { left: 605px; width: 551px; }

  .title { position: absolute; white-space: nowrap; font-weight: 400; }
  .title-script { font-family: "Great Vibes", cursive; font-weight: 400; line-height: 1; }
  .title-caps { font-family: "Marcellus", serif; line-height: 1; letter-spacing: 1px; }

  .back-title { left: 96px; top: 22px; display: flex; align-items: baseline; }
  .back-title .title-script { font-size: 112px; }
  .back-title .title-caps { font-size: 68px; margin-left: 6px; }

  .subtitle {
    position: absolute;
    font-family: "Marcellus SC", serif;
    text-align: center; white-space: nowrap; line-height: 1.05;
  }
  .subtitle-line { display: flex; align-items: center; justify-content: center; gap: 16px; }
  .subtitle-line::before, .subtitle-line::after {
    content: ""; display: block; width: 56px; height: 1.5px; background: var(--ink-light);
  }
  .subtitle-line:last-child::before, .subtitle-line:last-child::after { display: none; }
  .back-subtitle { left: 47px; width: 460px; top: 178px; font-size: 39px; }

  .blurb {
    position: absolute; left: 55px; top: 278px; width: 442px;
    font-family: "Montserrat", sans-serif; font-size: 13.4px; line-height: 20.5px;
    color: var(--ink-soft);
    text-align: justify; text-align-last: center;
  }
  .blurb p + p { margin-top: 12.5px; }

  .publisher {
    position: absolute; text-align: center;
    font-family: "Marcellus", serif; color: var(--ink-light); line-height: 1.35;
  }
  .publisher-name { display: block; font-size: 25px; }
  .publisher-line { display: block; font-size: 19px; letter-spacing: 3px; }
  .back-publisher { left: 58px; top: 722px; width: 170px; }
  .front-publisher { left: 198px; top: 36px; width: 170px; }

  .spine-text {
    position: absolute; left: 50%; top: 238px;
    transform-origin: 0 0; transform: translate(10px, 0) rotate(90deg);
    white-space: nowrap; display: flex; align-items: baseline; gap: 10px;
    font-family: "Marcellus SC", serif; font-size: 15px; color: var(--ink-light);
  }
  .spine-text .spine-script { font-family: "Great Vibes", cursive; font-size: 28px; color: var(--ink-dark); }
  .spine-text .spine-caps { font-family: "Marcellus", serif; font-size: 15px; color: var(--ink-dark); }
  .spine-divider { color: var(--ink-light); }

  .front-title { left: 0; top: 0; width: 551px; height: 520px; }
  .front-title .title-script {
    position: absolute; left: 70px; top: 200px; font-size: 186px;
  }
  .front-title .title-caps {
    position: absolute; left: 215px; top: 398px; font-size: 86px; letter-spacing: 0;
  }
  .front-subtitle { left: 45px; width: 460px; top: 704px; font-size: 39px; }
</style>
</head>
<body>
  <main class="spread">
    <div class="spread-photo" role="img" aria-label="Soft-focus photograph of a woman in white meditating outdoors, framed by blurred autumn leaves in red, orange and gold with a bright glowing sky behind her"></div>

    <section class="back-cover">
      <h2 class="title back-title">
        <span class="title-script">Quiet</span><span class="title-caps">BLOOM</span>
      </h2>
      <div class="subtitle back-subtitle">
        <div class="subtitle-line">Daily Practices</div>
        <div class="subtitle-line">For The Present Woman</div>
      </div>
      <div class="blurb">
        <p>Are you ready to embark on a transformative journey and elevate your daily existence? "Quiet Bloom" is a treasure trove of practical yet profound rituals and wisdom from renowned self-care, healing, and spirituality experts.</p>
        <p>Within these pages, you'll uncover a tapestry of guidance and insight from some of the world's most respected mentors. Their collective wisdom is your key to creating a sacred sanctuary within your everyday life.</p>
        <p>From invigorating morning rituals to meditative practices, empowering affirmations, and transformative energy healing, you'll find a rich tapestry of tools to nurture a deeper connection with yourself and the universe.</p>
        <p>Whether you're a seasoned practitioner or a newcomer to the world of self-care and spirituality, "Quiet Bloom" is your trusted companion on the journey to transform your life and elevate your daily experience. Open this book today and start your sacred, fulfilling adventure.</p>
      </div>
      <div class="publisher back-publisher">
        <span class="publisher-name">Lantern Grove</span>
        <span class="publisher-line">Publishing</span>
      </div>
    </section>

    <section class="spine">
      <div class="spine-text">
        <span class="spine-script">Quiet</span><span class="spine-caps">BLOOM</span>
        <span class="spine-divider">|</span>
        <span>Daily Practices For The Present Woman</span>
      </div>
    </section>

    <section class="front-cover">
      <div class="publisher front-publisher">
        <span class="publisher-name">Lantern Grove</span>
        <span class="publisher-line">Publishing</span>
      </div>
      <h1 class="title front-title">
        <span class="title-script">Quiet</span>
        <span class="title-caps">BLOOM</span>
      </h1>
      <div class="subtitle front-subtitle">
        <div class="subtitle-line">Daily Practices</div>
        <div class="subtitle-line">For The Present Woman</div>
      </div>
    </section>
  </main>
</body>
</html>
```